Redesign criminal justice consulting website

We run a small professional services firm that does research, evaluation, consulting, and training on criminal justice issues. We need to redesign our website (www.rvmetrics.com). The existing site is something we made ourselves. It is unprofessional and does not do a good job of communicating what we do or who we are.

We would like the new site to provide a basic overview of what we do. Moreover, we would like it to communicate several themes that represent who we are:

* global

* innovative

* analytical

* practical

We view the principal design challenge as figuring out a subtle, interesting, and graphically appealing way to communicate these themes.

Target Market(s)

Our primary customers are governments, research firms, criminal justice agencies, and schools. The people who we want to find our site are seeking research, evaluation, training, or consulting services related to crime, criminal justice, or policing.

Industry/Entity Type

Consulting

Number of Pages Required

2 pages

Requirements
Must have
• 1. We would like the site to use our logo. It is attached (please use the maroon 4-color version with the company name but without the slogan). The site should also use the colors present in our logo. It may use other colors as well, as long as these colors coordinate with the logo colors.

• 2. For main pages or buttons, we need the following:
• *Home
• *About RVM
• *Services
• *E-Training
• *Resources
• *Contact RVM

• 3. We like simple, crisp, subtle designs over "busier," cluttered, or very complex designs.

• 4. We'd like to receive, at a minimum, the home page and a sample inner page.
Nice to have
• We need some help in thinking through what regions or sections should exist on the home page. We are thinking about having a window on there where we can make announcements about recent developments like new reports, new e-training videos, new photographs, etc... We are open to suggestions here.
Should not have
• 1. Gimmicky or overused clipart.
• 2. Cliched images associated with criminal justice, including magnifying glasses, scales of justice, etc... Our logo makes a subtle nod to criminal justice through the use of a fingerprint as the dot on the "J" in the company initials. That''s sufficient for our purposes. Concentrate instead on the themes listed above.
• 3. Major use of colors that don't match our logo, like blue.

```html
<!DOCTYPE html>
<html lang="en">
<head>
<meta charset="utf-8">
<title>Research &amp; Value Metrics — Home Page Layouts</title>
<link rel="stylesheet" href="https://fonts.googleapis.com/css2?family=Crimson+Pro:wght@400;600&family=Kurale&display=swap">
<style>
  :root {
    --maroon: #8c1a3a;
    --maroon-dark: #6f1230;
    --gold: #f2b233;
    --gold-text: #e9b54c;
    --ink: #111111;
    --paper: #ffffff;
    --frame: #4a4a4a;
    --label-red: #e0201b;
    --muted: #d9d9d9;
  }
  * { box-sizing: border-box; margin: 0; padding: 0; }
  html, body { width: 900px; height: 1200px; overflow: hidden; background: var(--paper); }
  body { position: relative; font-family: "Kurale", Georgia, serif; color: var(--ink); }

  .layout { position: absolute; background: var(--paper); border: 1px solid var(--frame); overflow: hidden; }
  .layout--primary { left: 94px; top: 28px; width: 729px; height: 544px; }
  .layout--variant { left: 94px; top: 636px; width: 710px; height: 534px; }

  .variant-label {
    position: absolute; left: 96px; top: 593px;
    font-family: Arial, Helvetica, sans-serif; font-style: italic;
    font-size: 23px; color: var(--label-red);
  }

  /* Neutral name placeholder where the brand sits */
  .brand-name { position: absolute; display: flex; align-items: center; gap: 8px;
    font-family: "Crimson Pro", Georgia, serif; font-weight: 600; color: var(--maroon);
    line-height: 1; white-space: nowrap; }
  .brand-name__square { flex: none; background: var(--muted); }
  .layout--primary .brand-name { left: 30px; top: 44px; font-size: 30px; }
  .layout--primary .brand-name__square { width: 22px; height: 22px; }
  .layout--variant .brand-name { left: 592px; top: 452px; font-size: 18px; gap: 6px; }
  .layout--variant .brand-name__square { width: 13px; height: 13px; }

  .site-name { position: absolute; font-family: "Crimson Pro", Georgia, serif; font-weight: 600;
    color: var(--maroon); letter-spacing: 0.5px; line-height: 1; white-space: nowrap; }
  .layout--primary .site-name { left: 165px; top: 21px; width: 560px; text-align: center; font-size: 39px; }
  .layout--variant .site-name { left: 0; top: 45px; width: 100%; text-align: center; font-size: 43px; }

  .tagline { position: absolute; font-family: "Crimson Pro", Georgia, serif; font-weight: 600;
    font-size: 15px; letter-spacing: 2.2px; color: #222; white-space: nowrap; line-height: 1; }
  .layout--primary .tagline { right: 14px; top: 74px; }
  .layout--variant .tagline { left: 0; width: 100%; text-align: center; top: 28px; }

  .band { position: absolute; left: 0; width: 100%; }
  .band--dark { background: var(--ink); }
  .band--gold { background: var(--gold); height: 3px; }

  .main-nav { position: absolute; left: 0; width: 100%; height: 31px;
    background: linear-gradient(var(--maroon), var(--maroon-dark)); }
  .main-nav a { position: absolute; top: 6px; font-family: "Crimson Pro", Georgia, serif;
    font-weight: 600; font-size: 15.5px; letter-spacing: 0.6px; color: var(--paper); text-decoration: none; }
  .main-nav a.is-current { color: var(--gold); }
  .main-nav .tab { position: absolute; top: 0; width: 10px; height: 100%; background: rgba(0,0,0,0.12); }

  .hero-photo { position: absolute; background: var(--ink); display: flex; align-items: center;
    justify-content: center; color: var(--paper); font-size: 9.5px; letter-spacing: 0.3px; }
  .layout--primary .hero-photo { left: 16px; top: 198px; width: 142px; height: 176px; }
  .layout--variant .hero-photo { left: 16px; top: 196px; width: 137px; height: 171px; }

  .intro { position: absolute; font-size: 10.6px; line-height: 16.3px; color: var(--ink); white-space: nowrap; }
  .layout--primary .intro { left: 177px; top: 195px; }
  .layout--variant .intro { left: 172px; top: 193px; }

  .site-footer { position: absolute; left: 0; width: 100%; background: var(--ink);
    display: flex; align-items: center; justify-content: center; }
  .layout--primary .site-footer { top: 509px; height: 35px; }
  .layout--variant .site-footer { top: 498px; height: 36px; }
  .footer-links { font-family: "Crimson Pro", Georgia, serif; font-weight: 600; font-size: 10px;
    color: var(--gold-text); letter-spacing: 0.2px; white-space: nowrap; }
  .footer-links a { color: var(--gold-text); text-decoration: none; }
  .footer-links span { margin: 0 5px; }
</style>
</head>
<body>

<section class="layout layout--primary" aria-label="Home page layout">
  <div class="brand-name"><span class="brand-name__square"></span><span>RVM</span></div>
  <div class="site-name">RESEARCH &amp; VALUE METRICS</div>
  <div class="tagline">INNOVATIONS IN CRIME PREVENTION</div>

  <div class="band band--dark" style="top:101px;height:10px"></div>
  <div class="band band--gold" style="top:111px"></div>
  <nav class="main-nav" style="top:114px">
    <span class="tab" style="left:80px"></span><span class="tab" style="left:222px"></span>
    <span class="tab" style="left:352px"></span><span class="tab" style="left:480px"></span>
    <span class="tab" style="left:612px"></span>
    <a class="is-current" style="left:18px">Home</a>
    <a style="left:120px">About RVM</a>
    <a style="left:261px">Services</a>
    <a style="left:384px">E-Training</a>
    <a style="left:520px">Resource</a>
    <a style="left:641px">Contact</a>
  </nav>
  <div class="band band--gold" style="top:146px"></div>
  <div class="band band--dark" style="top:149px;height:11px"></div>

  <div class="hero-photo" role="img" aria-label="Feature photograph of the team or their work">IMAGE / YOUR PHOTO</div>
  <p class="intro">
    Research and Value Metrics, Inc. is a consulting firm based in Northern Virginia near Washington, DC.<br>
    We specialize in providing training, technical assistance, research, evaluation and other services related<br>
    to crime prevention and criminal<br>
    justice. Our services are provided by a network of experts with a variety of backgrounds in social science,<br>
    law enforcement, criminal law, forensics, and other professions.<br>
    Projects range in scope from brief consultations, reports, or training sessions to comprehensive,<br>
    multi-year system-wide transformation efforts. Our clients include governments, public agencies,<br>
    professional associations, universities and research centers, non-governmental organizations, and professional<br>
    services firms.&nbsp; We also have significant international experience and have worked in both developed and<br>
    developing nations. We specialize in working closely with our clients to design tailored, innovative solutions.<br>
    Call today and explore how we can be of service
  </p>

  <footer class="site-footer">
    <div class="footer-links"><a>Home</a><span>-</span><a>About RVM</a><span>-</span><a>Services</a><span>-</span><a>E-Training</a><span>-</span><a>Resource</a><span>-</span><a>Contact RVM</a></div>
  </footer>
</section>

<div class="variant-label">Variant</div>

<section class="layout layout--variant" aria-label="Home page layout, variant">
  <div class="tagline">INNOVATIONS IN CRIME PREVENTION</div>
  <div class="site-name">RESEARCH &amp; VALUE METRICS</div>

  <div class="band band--dark" style="top:100px;height:10px"></div>
  <div class="band band--gold" style="top:110px"></div>
  <nav class="main-nav" style="top:113px">
    <span class="tab" style="left:78px"></span><span class="tab" style="left:218px"></span>
    <span class="tab" style="left:346px"></span><span class="tab" style="left:474px"></span>
    <span class="tab" style="left:598px"></span>
    <a class="is-current" style="left:17px">Home</a>
    <a style="left:117px">About RVM</a>
    <a style="left:255px">Services</a>
    <a style="left:376px">E-Training</a>
    <a style="left:507px">Resource</a>
    <a style="left:626px">Contact</a>
  </nav>
  <div class="band band--gold" style="top:145px"></div>
  <div class="band band--dark" style="top:148px;height:12px"></div>

  <div class="hero-photo" role="img" aria-label="Feature photograph of the team or their work">IMAGE / YOUR PHOTO</div>
  <p class="intro">
    Research and Value Metrics, Inc. is a consulting firm based in Northern Virginia near Washington, DC.<br>
    We specialize in providing training, technical assistance, research, evaluation and other services related<br>
    to crime prevention and criminal<br>
    justice. Our services are provided by a network of experts with a variety of backgrounds in social science,<br>
    law enforcement, criminal law, forensics, and other professions.<br>
    Projects range in scope from brief consultations, reports, or training sessions to comprehensive,<br>
    multi-year system-wide transformation efforts. Our clients include governments, public agencies,<br>
    professional associations, universities and research centers, non-governmental organizations, and professional<br>
    services firms.&nbsp; We also have significant international experience and have worked in both developed and<br>
    developing nations. We specialize in working closely with our clients to design tailored, innovative solutions.<br>
    Call today and explore how we can be of service
  </p>

  <div class="brand-name"><span class="brand-name__square"></span><span>RVM</span></div>

  <footer class="site-footer">
    <div class="footer-links"><a>Home</a><span>-</span><a>About RVM</a><span>-</span><a>Services</a><span>-</span><a>E-Training</a><span>-</span><a>Resource</a><span>-</span><a>Contact RVM</a></div>
  </footer>
</section>

</body>
</html>
```